Football/Sports Motivational Poster

Use the picture provided. Crop the lady out to the right. At the top of the poster "Pressure Is A Privilege"
At the bottom of the poster "Prove Them Wrong"
Vertical Poster. Must look Bad Ass! Also include various high res files

```html
<!DOCTYPE html>
<html lang="en">
<head>
<meta charset="UTF-8">
<title>Pressure Is A Privilege – Football Poster</title>
<link rel="stylesheet" href="https://fonts.googleapis.com/css2?family=Graduate&family=Oswald:wght@500;600;700&display=swap">
<style>
  :root {
    --night: #141018;
    --night-purple: #2a2230;
    --gold: #f6b40e;
    --gold-bright: #f9d21c;
    --gold-deep: #c9780a;
    --headline-yellow: #f2dc12;
    --ink: #231d22;
    --fog: #8d8b8e;
    --ground: #1b1a1c;
    --white: #f4f3f1;
  }
  html, body {
    margin: 0;
    padding: 0;
    width: 671px;
    height: 1200px;
    overflow: hidden;
    background: var(--night);
  }
  .poster {
    position: relative;
    width: 671px;
    height: 1200px;
    overflow: hidden;
  }
  .poster-art {
    position: absolute;
    inset: 0;
    display: block;
  }
  .kicker {
    font-family: "Oswald", "Arial Narrow", sans-serif;
    font-weight: 600;
  }
  .headline {
    font-family: "Graduate", "Georgia", serif;
  }
  .tagline {
    font-family: "Oswald", "Arial Narrow", sans-serif;
    font-weight: 700;
  }
</style>
</head>
<body>
<main class="poster">
  <svg class="poster-art" width="671" height="1200" viewBox="0 0 671 1200" xmlns="http://www.w3.org/2000/svg">
    <defs>
      <linearGradient id="night-sky" x1="0" y1="0" x2="0" y2="1">
        <stop offset="0" stop-color="#2b2530"/>
        <stop offset="0.5" stop-color="#17121a"/>
        <stop offset="1" stop-color="#100d12"/>
      </linearGradient>
      <linearGradient id="gold-field" x1="0" y1="0" x2="0.4" y2="1">
        <stop offset="0" stop-color="#f7a80c"/>
        <stop offset="0.45" stop-color="#f6b812"/>
        <stop offset="1" stop-color="#e9a40e"/>
      </linearGradient>
      <linearGradient id="fog-floor" x1="0" y1="0" x2="0" y2="1">
        <stop offset="0" stop-color="#9a989b" stop-opacity="0"/>
        <stop offset="0.35" stop-color="#8f8d90" stop-opacity="0.75"/>
        <stop offset="0.7" stop-color="#5b595c"/>
        <stop offset="1" stop-color="#1b1a1c"/>
      </linearGradient>
      <linearGradient id="players-tone" x1="0" y1="0" x2="1" y2="0">
        <stop offset="0" stop-color="#3b3540" stop-opacity="0.7"/>
        <stop offset="0.45" stop-color="#d9d8d6" stop-opacity="0.85"/>
        <stop offset="0.6" stop-color="#b8a24a" stop-opacity="0.55"/>
        <stop offset="1" stop-color="#c98a10" stop-opacity="0.45"/>
      </linearGradient>
      <clipPath id="dark-side">
        <polygon points="0,0 469,0 84,1200 0,1200"/>
      </clipPath>
      <clipPath id="gold-side">
        <polygon points="469,0 671,0 671,1200 84,1200"/>
      </clipPath>
    </defs>

    <!-- background split -->
    <rect class="bg-night" width="671" height="1200" fill="url(#night-sky)"/>
    <polygon class="bg-gold" points="475,0 671,0 671,1200 88,1200" fill="url(#gold-field)"/>
    <polygon class="bg-gold-edge" points="452,0 478,0 92,1200 66,1200" fill="var(--gold-deep)" opacity="0.55"/>

    <!-- big jersey numeral outline -->
    <g class="numeral-outline" fill="none" stroke="#f4f3f1" stroke-opacity="0.45" stroke-width="2">
      <path d="M470 188 H671 M422 236 L470 188 M422 236 V530 L450 560 L422 590 V826 L470 874 H671"/>
      <rect x="519" y="321" width="112" height="153" rx="4"/>
      <rect x="519" y="598" width="112" height="153" rx="4"/>
    </g>

    <!-- photo area -->
    <rect class="photo-players" x="43" y="170" width="602" height="950" rx="6" fill="url(#players-tone)" role="img" aria-label="Photo: football player in white jersey walking off the field, helmet in hand, head down, with a larger golden-lit player behind him"/>

    <!-- fog and ground -->
    <rect class="fog-floor" x="0" y="700" width="671" height="500" fill="url(#fog-floor)"/>

    <!-- top headline -->
    <text class="kicker" x="55" y="123" font-size="45" fill="var(--headline-yellow)" letter-spacing="2" textLength="300" lengthAdjust="spacingAndGlyphs">PRESSURE IS A</text>

    <g class="headline" font-size="150">
      <text x="55" y="272" textLength="570" lengthAdjust="spacingAndGlyphs" fill="var(--white)" stroke="var(--headline-yellow)" stroke-width="3" paint-order="stroke" clip-path="url(#dark-side)">PRIVILEGE</text>
      <text x="55" y="272" textLength="570" lengthAdjust="spacingAndGlyphs" fill="var(--ink)" stroke="var(--night)" stroke-width="2" paint-order="stroke" clip-path="url(#gold-side)">PRIVILEGE</text>
    </g>

    <!-- bottom tagline -->
    <g class="tagline" text-anchor="end">
      <text x="627" y="953" font-size="52" fill="var(--white)" textLength="95" lengthAdjust="spacingAndGlyphs">PROVE</text>
      <text x="627" y="997" font-size="52" fill="var(--white)" textLength="78" lengthAdjust="spacingAndGlyphs">THEM</text>
      <text x="627" y="1097" font-size="110" fill="var(--gold-bright)" stroke="var(--white)" stroke-width="2.5" paint-order="stroke" textLength="272" lengthAdjust="spacingAndGlyphs">WRONG</text>
    </g>
  </svg>
</main>
</body>
</html>
```